KVT Website Homepage Redesign

My website needs a homepage redesign and banner photos updates for Discovery and SEO Services pages. We sell Search Engine Optimization services. We use Search Engine Optimization techniques to help our clients rank high in search engines like Zorvix. It is an intense competition to consistently rank above other businesses. The problem is there is no easy way to show what the benefits of Search Engine Optimization services look like in an emotional way. I want to use an image from sailboat racing to dramatize that our clients win at Search Engine Optimization marketing.
The following products are desired:
1. Desktop version homepage redesign with a banner that clearly shows we sell Search Engine Optimization services using sailboat racing as a metaphor.
2. Mobile version homepage redesign with a banner that clearly shows we sell Search Engine Optimization services using sailboat racing as a metaphor.
2. New banner photo for the Discovery Page
3. New banner photo for the SEO page
The design must be responsive and show well on desktops, laptops, tablets and mobile phones. The current footer style must be kept. A third service called SEO must be added.
the website URL is www.brightfernlabs.example
Target Market(s)
Business to Business
Industry/Entity Type
Digital Marketing
Coding
Coded - Design and coding required
Number of Pages Required
1 page
Colors
Designer to choose colors to be used in the design.
Look and feel
Each slider illustrates characteristics of the customer's brand and the style your logo design should communicate.

```html
<!DOCTYPE html>
<html lang="en">
<head>
<meta charset="utf-8">
<title>KVT Applications — Homepage</title>
<link rel="stylesheet" href="https://fonts.googleapis.com/css2?family=Open+Sans:wght@400;600;700&display=swap">
<style>
:root{
  --blue:#3a6fc4;
  --blue-mid:#4a7bc8;
  --blue-band:#6d98da;
  --blue-foot:#7ba3e0;
  --card:#e7effc;
  --ink:#1f2430;
  --body:#3d4250;
  --gold:#f5b400;
  --white:#ffffff;
  --line:#8a8f9c;
}
*{box-sizing:border-box;margin:0;padding:0}
html,body{width:1200px;height:5280px;overflow:hidden;background:var(--white)}
body{font-family:"Open Sans",Arial,sans-serif;color:var(--ink)}
.page{position:relative;width:1200px;height:5280px;overflow:hidden}
.abs{position:absolute}

/* header */
.brand{left:51px;top:18px;color:var(--blue);font-weight:600;font-size:40px;line-height:44px;display:flex;align-items:center;gap:12px}
.brand-dot{width:16px;height:16px;border-radius:50%;background:var(--gold)}
.nav{right:46px;top:36px;display:flex;gap:38px;font-size:26px;color:var(--blue)}
.nav a{color:inherit;text-decoration:none;position:relative}
.nav a.active{color:var(--gold)}
.nav a.active::after{content:"";position:absolute;left:50%;top:44px;width:8px;height:8px;margin-left:-4px;border-radius:50%;background:var(--gold)}

/* hero */
.hero{left:0;top:113px;width:1200px;height:677px;background:linear-gradient(90deg,#8a8f98 0%,#a7adb6 35%,#c6cdd6 70%,#d9dee5 100%)}
.hero-rule{left:0;top:786px;width:1200px;height:8px;background:var(--gold)}
.hero-sail{left:599px;top:148px;width:606px;height:606px;border-radius:50%;background:linear-gradient(180deg,#9fc1e8 0%,#5f87b8 55%,#25406b 100%)}
.hero-title{left:51px;top:468px;font-size:66px;line-height:80px;font-weight:700;color:var(--gold)}

/* mission */
.mission-photo{left:82px;top:892px;width:359px;height:276px;background:linear-gradient(135deg,#e9e4de,#c7ccd4);box-shadow:0 10px 30px rgba(58,111,196,.18)}
.bubble{width:40px;height:40px;border-radius:50%;background:var(--white);box-shadow:0 4px 12px rgba(58,111,196,.25);display:flex;align-items:center;justify-content:center}
.bubble i{width:14px;height:14px;border-radius:50%;background:#f3c14a;display:block}
.mission{left:547px;top:922px;width:600px;font-size:29px;line-height:56px;letter-spacing:1.5px;color:var(--blue);text-transform:uppercase}
.mission strong{color:var(--ink);font-weight:700}
.arc{left:760px;top:800px;width:560px;height:560px;border-radius:50%;border:30px solid rgba(58,111,196,.05)}

/* services */
.icon-tile{width:134px;height:134px;border-radius:30px;background:var(--blue-mid);display:flex;align-items:center;justify-content:center;box-shadow:0 12px 30px rgba(58,111,196,.3)}
.dots{display:grid;grid-template-columns:repeat(6,6px);gap:14px 14px}
.dots span{width:6px;height:6px;border-radius:50%;background:var(--blue-mid)}
.section-title{font-size:32px;font-weight:600;letter-spacing:1px;color:var(--ink);line-height:52px}
.section-copy{font-size:15px;line-height:30px;color:var(--body)}

.card{border-radius:14px;background:var(--card);text-align:center;padding:0 22px;color:var(--body)}
.card .icon{display:block;margin:0 auto}
.card h3{font-size:18px;font-weight:400;color:var(--ink);letter-spacing:.5px;margin:12px 0 8px}
.card p{font-size:15px;line-height:25px}
.card .go{position:absolute;right:16px;bottom:14px}
.card.featured{background:var(--blue-mid);color:var(--white)}
.card.featured h3{color:var(--white)}

/* clients */
.h2{font-size:29px;font-weight:700;color:var(--ink);letter-spacing:.5px}
.sub{font-size:29px;font-weight:600;color:var(--blue)}
.checks{left:51px;top:3196px;list-style:none}
.checks li{position:absolute;left:0;width:470px;padding-left:66px;font-size:27px;line-height:36px;color:var(--blue);letter-spacing:.5px;white-space:nowrap}
.checks li::before{content:"";position:absolute;left:0;top:4px;width:32px;height:32px;border-radius:5px;background:var(--blue-mid)}
.checks li svg{position:absolute;left:6px;top:10px}
.client-bg{left:553px;top:3198px;width:369px;height:451px;background:linear-gradient(180deg,#b8cfe8,#3e6494)}
.client-shot{left:611px;top:3245px;width:543px;height:353px;background:linear-gradient(180deg,#f4f4f4 0%,#f4f4f4 10%,#5c5c5c 10%,#7b7b7b 48%,#9b1f5e 48%,#9b1f5e 55%,#fbfbfb 55%);border:1px solid #d6dbe4;box-shadow:0 8px 22px rgba(0,0,0,.12)}

/* cta */
.cta{left:0;top:3813px;width:1200px;height:369px;background:var(--blue-band)}
.cta-kicker{left:51px;top:3855px;font-size:25px;color:var(--white);letter-spacing:1px}
.cta-title{left:51px;top:3918px;font-size:56px;font-weight:600;color:var(--gold);letter-spacing:1px}
.btn-light{left:51px;top:4063px;width:177px;height:53px;background:var(--white);color:var(--blue);font-size:25px;letter-spacing:1px;display:flex;align-items:center;justify-content:center}
.device{left:822px;top:3762px;width:212px;height:461px;border-radius:32px;background:linear-gradient(180deg,#fbfcfe,#e9eef6);box-shadow:0 16px 40px rgba(0,0,0,.18)}
.device-card{left:697px;top:3870px;width:152px;height:140px;background:#fff;border-radius:6px;box-shadow:0 6px 18px rgba(0,0,0,.12)}
.device-card2{left:945px;top:4020px;width:152px;height:100px;background:#fff;border-radius:6px;box-shadow:0 6px 18px rgba(0,0,0,.12)}

/* form */
.form-title{left:51px;top:4256px;font-size:30px;font-weight:600}
.label{font-size:19px;color:var(--ink)}
.label b{color:#d23c3c;font-weight:400}
.field{height:52px;border:1px solid var(--line);background:#fff}
.captcha{left:857px;top:4584px;width:152px;height:51px;background:var(--blue-mid);color:#fff;font-weight:700;font-size:22px;display:flex;align-items:center;justify-content:center;letter-spacing:2px}
.refresh{left:1009px;top:4584px;width:57px;height:51px;border:1px solid var(--blue-mid);display:flex;align-items:center;justify-content:center}
.submit{left:506px;top:4700px;width:187px;height:50px;background:var(--blue-mid);color:#fff;font-size:27px;font-weight:600;letter-spacing:1px;display:flex;align-items:center;justify-content:center}

/* footer */
.footer{left:0;top:4828px;width:1200px;height:452px;background:linear-gradient(180deg,#86acE4,#6f98d8)}
.wheel{left:51px;top:4904px;width:263px;height:263px;border-radius:50%;background:#4f7cc4;border:14px solid #dfe8f7;display:flex;align-items:center;justify-content:center}
.wheel-core{width:120px;height:120px;border-radius:50%;background:#fff;display:flex;align-items:center;justify-content:center;color:var(--blue);font-size:19px;font-weight:600}
.foot-h{font-size:34px;color:var(--ink);letter-spacing:1px}
.foot-list{font-size:19px;line-height:37px;color:var(--ink);list-style:none}
.copy{left:0;top:5223px;width:1200px;text-align:center;font-size:18px;color:var(--ink)}
</style>
</head>
<body>
<div class="page">

  <!-- header -->
  <div class="abs brand"><span class="brand-dot"></span>KVT Applications</div>
  <nav class="abs nav"><a class="active" href="#">Info</a><a href="#">Let's Talk</a><a href="#">Support</a></nav>

  <!-- hero -->
  <div class="abs hero" role="img" aria-label="Photo of two colleagues working together at a laptop"></div>
  <div class="abs hero-sail" role="img" aria-label="Circular photo of racing sailboats on open water"></div>
  <div class="abs hero-rule"></div>
  <h1 class="abs hero-title">Are you ready<br>to take the lead?</h1>

  <!-- mission -->
  <div class="abs arc"></div>
  <div class="abs mission-photo" role="img" aria-label="Collage photo of a person working at a laptop"></div>
  <div class="abs bubble" style="left:146px;top:856px"><i></i></div>
  <div class="abs bubble" style="left:154px;top:1154px"><i style="background:#5fb85f;border-radius:2px;width:12px"></i></div>
  <p class="abs mission"><strong>Our mission</strong> is to empower every client with the web presence that will drive them ahead of the competition.</p>

  <!-- SEO consulting -->
  <div class="abs dots" style="left:157px;top:1333px">
    <span></span><span></span><span></span><span></span><span></span><span></span>
    <span></span><span></span><span></span><span></span><span></span><span></span>
    <span></span><span></span><span></span><span></span><span></span><span></span>
    <span></span><span></span><span></span><span></span><span></span><span></span>
    <span></span><span></span><span></span><span></span><span></span><span></span>
    <span></span><span></span><span></span><span></span><span></span><span></span>
  </div>
  <div class="abs icon-tile" style="left:62px;top:1363px">
    <svg width="72" height="64" viewBox="0 0 72 64" fill="none" stroke="#f5b400" stroke-width="3"><rect x="6" y="6" width="60" height="40" rx="3"/><path d="M2 52h68M20 18h32M20 28h20"/><circle cx="50" cy="30" r="6"/></svg>
  </div>
  <h2 class="abs section-title" style="left:51px;top:1563px">SEO CONSULTING</h2>
  <p class="abs section-copy" style="left:51px;top:1636px;width:400px">Search Engine Optimization is a term always on the tip of the tongue of web marketing and web development experts, and this is for good reason. SEO is the process of affecting the online visibility of a website through the construction of the website itself. When done well, these efforts extend from the backend code and structural elements to the design and content of specific pages.</p>

  <div class="abs card featured" style="left:480px;top:1292px;width:320px;height:338px;padding-top:26px">
    <svg class="icon" width="70" height="70" viewBox="0 0 70 70" fill="none" stroke="#f5b400" stroke-width="3"><circle cx="30" cy="30" r="18"/><path d="M12 30h36M30 12v36M43 43l16 16"/></svg>
    <h3>DISCOVERY</h3>
    <p>Understanding your business goals informs the design and development phases, all of which enable your website to do more</p>
    <svg class="go" width="36" height="36" viewBox="0 0 36 36"><circle cx="18" cy="18" r="16" fill="none" stroke="#fff" stroke-width="2"/><path d="M14 10l10 8-10 8z" fill="#fff"/></svg>
  </div>
  <div class="abs card" style="left:830px;top:1328px;width:322px;height:337px;padding-top:20px">
    <svg class="icon" width="70" height="70" viewBox="0 0 70 70" fill="none" stroke="#3a6fc4" stroke-width="3"><rect x="10" y="12" width="50" height="34" rx="3"/><path d="M4 54h62"/><circle cx="42" cy="30" r="10"/></svg>
    <h3>SEARCH ENGINE OPTIMIZATION</h3>
    <p>A website built with a strong SEO base is essential. Powerful search engine optimization means higher placement on search engine results pages and more visitors on your website. Everything begins there.</p>
    <svg class="go" width="36" height="36" viewBox="0 0 36 36"><circle cx="18" cy="18" r="16" fill="none" stroke="#3a6fc4" stroke-width="2"/><path d="M14 10l10 8-10 8z" fill="#3a6fc4"/></svg>
  </div>
  <div class="abs card" style="left:482px;top:1656px;width:320px;height:337px;padding-top:20px">
    <svg class="icon" width="70" height="70" viewBox="0 0 70 70" fill="none" stroke="#3a6fc4" stroke-width="3"><circle cx="35" cy="35" r="16"/><circle cx="35" cy="35" r="6"/><path d="M35 8v10M35 52v10M8 35h10M52 35h10"/></svg>
    <h3>LOCAL OPTIMIZATION</h3>
    <p>When online audiences can find businesses in their own backyard to answer all of their needs, your business can win—as long as your web strategy is prepared for these local queries</p>
    <svg class="go" width="36" height="36" viewBox="0 0 36 36"><circle cx="18" cy="18" r="16" fill="none" stroke="#3a6fc4" stroke-width="2"/><path d="M14 10l10 8-10 8z" fill="#3a6fc4"/></svg>
  </div>
  <div class="abs card" style="left:832px;top:1693px;width:320px;height:339px;padding-top:20px">
    <svg class="icon" width="70" height="70" viewBox="0 0 70 70" fill="none" stroke="#3a6fc4" stroke-width="3"><circle cx="35" cy="35" r="24" stroke-dasharray="4 4"/><text x="35" y="45" text-anchor="middle" font-size="30" fill="#3a6fc4" stroke="none" font-family="Open Sans,sans-serif">$</text></svg>
    <h3>PPC</h3>
    <p>Beyond organic SEO strategies, Pay-Per-Click (PPC) tactics are one more way to get your business in front of your customers' eyes online, and this is one of our favorite marketing strategies.</p>
    <svg class="go" width="36" height="36" viewBox="0 0 36 36"><circle cx="18" cy="18" r="16" fill="none" stroke="#3a6fc4" stroke-width="2"/><path d="M14 10l10 8-10 8z" fill="#3a6fc4"/></svg>
  </div>

  <!-- website design -->
  <div class="abs card" style="left:49px;top:2146px;width:322px;height:339px;padding-top:20px">
    <svg class="icon" width="70" height="70" viewBox="0 0 70 70" fill="none" stroke="#3a6fc4" stroke-width="3"><rect x="8" y="10" width="44" height="40" rx="2"/><path d="M16 22h28M16 32h20M16 42h24"/><circle cx="54" cy="18" r="8"/></svg>
    <h3>WEBSITE STRATEGY</h3>
    <p>A strong company website increases leads and reduces bounces by giving a visitor exactly what they're looking for and hooks them with both helpfulness and expertise.</p>
    <svg class="go" width="36" height="36" viewBox="0 0 36 36"><circle cx="18" cy="18" r="16" fill="none" stroke="#3a6fc4" stroke-width="2"/><path d="M14 10l10 8-10 8z" fill="#3a6fc4"/></svg>
  </div>
  <div class="abs card" style="left:400px;top:2183px;width:320px;height:339px;padding-top:20px">
    <svg class="icon" width="70" height="70" viewBox="0 0 70 70" fill="none" stroke="#3a6fc4" stroke-width="3"><rect x="10" y="10" width="50" height="36" rx="2"/><path d="M4 54h62M18 22h20M18 32h14M44 38l10-18"/></svg>
    <h3>WEB WRITING SERVICES</h3>
    <p>Well-crafted web writing is a balancing act between message, brand voice, audience expectation, and SEO. Our experienced writing and editing team is ready when you are.</p>
    <svg class="go" width="36" height="36" viewBox="0 0 36 36"><circle cx="18" cy="18" r="16" fill="none" stroke="#3a6fc4" stroke-width="2"/><path d="M14 10l10 8-10 8z" fill="#3a6fc4"/></svg>
  </div>
  <div class="abs card" style="left:49px;top:2511px;width:322px;height:339px;padding-top:20px">
    <svg class="icon" width="70" height="70" viewBox="0 0 70 70" fill="none" stroke="#3a6fc4" stroke-width="3"><rect x="6" y="12" width="50" height="34" rx="2"/><path d="M18 22v16M26 22v16M34 30h14M60 24l6 6-6 6"/></svg>
    <h3>ADVANCED WEB TOOLS</h3>
    <p>CRM or API integration, ecommerce capabilities, advanced calendars and forms—whatever you might need, we can make it happen for you.</p>
    <svg class="go" width="36" height="36" viewBox="0 0 36 36"><circle cx="18" cy="18" r="16" fill="none" stroke="#3a6fc4" stroke-width="2"/><path d="M14 10l10 8-10 8z" fill="#3a6fc4"/></svg>
  </div>
  <div class="abs card" style="left:402px;top:2548px;width:320px;height:338px;padding-top:20px">
    <svg class="icon" width="70" height="70" viewBox="0 0 70 70" fill="none" stroke="#3a6fc4" stroke-width="3"><rect x="8" y="10" width="40" height="12" rx="2"/><rect x="8" y="26" width="40" height="12" rx="2"/><rect x="8" y="42" width="40" height="12" rx="2"/><circle cx="54" cy="38" r="10"/><path d="M49 38l4 4 6-7"/></svg>
    <h3>HOSTING &amp; SUPPORT</h3>
    <p>A reliable hosting environment is the difference between a website that is fast or slow, vulnerable to attack or secure, backed-up or not.</p>
    <svg class="go" width="36" height="36" viewBox="0 0 36 36"><circle cx="18" cy="18" r="16" fill="none" stroke="#3a6fc4" stroke-width="2"/><path d="M14 10l10 8-10 8z" fill="#3a6fc4"/></svg>
  </div>

  <div class="abs dots" style="left:945px;top:2205px">
    <span></span><span></span><span></span><span></span><span></span><span></span>
    <span></span><span></span><span></span><span></span><span></span><span></span>
    <span></span><span></span><span></span><span></span><span></span><span></span>
    <span></span><span></span><span></span><span></span><span></span><span></span>
    <span></span><span></span><span></span><span></span><span></span><span></span>
    <span></span><span></span><span></span><span></span><span></span><span></span>
  </div>
  <div class="abs icon-tile" style="left:1006px;top:2234px">
    <svg width="72" height="64" viewBox="0 0 72 64" fill="none" stroke="#f5b400" stroke-width="3"><rect x="6" y="6" width="60" height="42" rx="3"/><path d="M6 16h60M14 26h20M14 36h14"/><rect x="40" y="24" width="18" height="16"/></svg>
  </div>
  <h2 class="abs section-title" style="right:44px;top:2444px;text-align:right;width:460px">WEBSITE DESIGN,<br>DEVELOPMENT &amp; HOSTING</h2>
  <p class="abs section-copy" style="left:752px;top:2576px;width:404px;text-align:center">A new website should be an all-device experience, requiring minimal clicks to bring a visitor exactly where they want to go, no matter whether they are browsing from their smartphone, tablet, or PC. Its design should be modern and accessible, recognizing that different demographics respond differently to different layout, content, and visual choices. A website should be optimized for text &amp; voice considering the possibilities of local search or international translation needs.</p>

  <!-- who we work with -->
  <h2 class="abs h2" style="left:51px;top:3070px">WHO DO WE WORK WITH?</h2>
  <p class="abs sub" style="left:607px;top:3112px">Here's KVT Application clients</p>
  <ul class="abs checks">
    <li style="top:0"><svg width="20" height="16" viewBox="0 0 20 16"><path d="M2 8l6 6L18 2" fill="none" stroke="#fff" stroke-width="3"/></svg>STARTUPS</li>
    <li style="top:74px"><svg width="20" height="16" viewBox="0 0 20 16"><path d="M2 8l6 6L18 2" fill="none" stroke="#fff" stroke-width="3"/></svg>SMALL TO MEDIUM-SIZED<br>BUSINESSES</li>
    <li style="top:184px"><svg width="20" height="16" viewBox="0 0 20 16"><path d="M2 8l6 6L18 2" fill="none" stroke="#fff" stroke-width="3"/></svg>NONPROFITS GOVERNMENT<br>AGENCIES</li>
    <li style="top:294px"><svg width="20" height="16" viewBox="0 0 20 16"><path d="M2 8l6 6L18 2" fill="none" stroke="#fff" stroke-width="3"/></svg>ECOMMERCE MARKETPLACES</li>
  </ul>
  <div class="abs client-bg" role="img" aria-label="Photo of a sailboat on the water"></div>
  <div class="abs client-shot" role="img" aria-label="Screenshot of a client's homepage"></div>
  <div class="abs bubble" style="left:982px;top:3190px"><i></i></div>
  <div class="abs bubble" style="left:992px;top:3618px;width:46px;height:46px">
    <svg width="30" height="30" viewBox="0 0 36 36"><circle cx="18" cy="18" r="16" fill="none" stroke="#3a6fc4" stroke-width="2"/><path d="M14 10l10 8-10 8z" fill="#3a6fc4"/></svg>
  </div>

  <!-- call to action -->
  <div class="abs cta"></div>
  <p class="abs cta-kicker">LET'S GET STARTED</p>
  <p class="abs cta-title">READY TO BEGIN?</p>
  <div class="abs btn-light">CONTACT</div>
  <div class="abs device" role="img" aria-label="Illustration of a phone showing an analytics dashboard"></div>
  <div class="abs device-card" role="img" aria-label="Bar chart card"></div>
  <div class="abs device-card2" role="img" aria-label="Bounce rate gauge card"></div>
  <div class="abs bubble" style="left:745px;top:4040px"><i></i></div>
  <div class="abs bubble" style="left:1062px;top:3860px"><i style="background:#3a6fc4;border-radius:2px;width:12px"></i></div>

  <!-- contact form -->
  <h2 class="abs form-title">CONTACT US</h2>
  <label class="abs label" style="left:137px;top:4332px">First Name <b>*</b></label>
  <div class="abs field" style="left:137px;top:4362px;width:429px"></div>
  <label class="abs label" style="left:636px;top:4332px">Last Name <b>*</b></label>
  <div class="abs field" style="left:636px;top:4362px;width:430px"></div>
  <label class="abs label" style="left:137px;top:4439px">Email <b>*</b></label>
  <div class="abs field" style="left:137px;top:4469px;width:429px"></div>
  <label class="abs label" style="left:636px;top:4439px">Company <b>*</b></label>
  <div class="abs field" style="left:636px;top:4469px;width:430px"></div>
  <label class="abs label" style="left:137px;top:4552px">Phone <b>*</b></label>
  <div class="abs field" style="left:137px;top:4584px;width:429px"></div>
  <label class="abs label" style="left:636px;top:4552px">Enter the Captcha</label>
  <div class="abs field" style="left:636px;top:4584px;width:114px"></div>
  <div class="abs captcha">fr5hM</div>
  <div class="abs refresh"><svg width="30" height="30" viewBox="0 0 30 30" fill="none" stroke="#3a6fc4" stroke-width="3"><path d="M24 12a10 10 0 0 0-18-2M6 18a10 10 0 0 0 18 2"/><path d="M6 4v6h6M24 26v-6h-6"/></svg></div>
  <div class="abs submit">SUBMIT</div>

  <!-- footer -->
  <div class="abs footer"></div>
  <div class="abs wheel" role="img" aria-label="Circular diagram of service steps"><div class="wheel-core">KVT</div></div>
  <h3 class="abs foot-h" style="left:394px;top:4918px">LOCATION</h3>
  <ul class="abs foot-list" style="left:394px;top:4987px">
    <li>482 Harborlight Way</li><li>Suite 210</li><li>Westmere, MD 20990</li>
  </ul>
  <h3 class="abs foot-h" style="left:760px;top:4918px">USEFUL LINKS</h3>
  <ul class="abs foot-list" style="left:765px;top:4985px">
    <li>Home</li><li>Web Strategy</li><li>Support</li><li>Privacy</li>
  </ul>
  <ul class="abs foot-list" style="left:939px;top:4985px">
    <li>SEO</li><li>Advanced Website Tools</li><li>Testimonials</li><li>Terms of Use</li>
  </ul>
  <p class="abs copy">© 2020 KVT Applications | All Rights Reserved | Web Strategy by KVT Applications</p>

</div>
</body>
</html>
```